Plakat-Design für Chor und Blasorchester
Zielgruppe
Konzert eines Orchesters zusammen mit drei Chören.
Zielgruppe Musikinteressierte allen Alters
(Alter der Musiker/Sänger 15-85)
Aufgabenstellung
PLakat wird in erster Linie in A3 und A4 gedruck.
Vermutlich machen wir auch Flyer

```html
<!DOCTYPE html>
<html lang="de">
<head>
<meta charset="utf-8">
<title>Ohrwürmer – Konzertplakat</title>
<link rel="stylesheet" href="https://fonts.googleapis.com/css2?family=Roboto:wght@900&family=Roboto+Condensed:wght@400;700&display=swap">
<style>
  :root {
    --paper: #ffffff;
    --title-red: #d0191b;
    --ink: #111111;
    --badge: #0d0d0d;
    --badge-text: #ffffff;
    --art-red: #e2231a;
    --art-orange: #f28a1c;
    --art-blue: #1f5fb5;
    --art-pink: #e45a8f;
  }
  * { margin: 0; padding: 0; box-sizing: border-box; }
  html, body { width: 848px; height: 1200px; overflow: hidden; background: var(--paper); }
  .poster { position: relative; width: 848px; height: 1200px; background: var(--paper); overflow: hidden; font-family: "Roboto Condensed", "Arial Narrow", sans-serif; color: var(--ink); }
  .title { position: absolute; left: 36px; top: 60px; width: 772px; height: 120px; }
  .title text { font-family: "Roboto", Arial, sans-serif; font-weight: 900; fill: var(--title-red); }
  .subtitle { position: absolute; right: 46px; top: 183px; text-align: right; font-size: 29px; line-height: 37px; }
  .art { position: absolute; }
  .art-birds { left: 110px; top: 215px; width: 190px; height: 140px; border-radius: 50%;
    background: radial-gradient(ellipse at center, rgba(226,35,26,.35), rgba(31,95,181,.15) 55%, transparent 72%); }
  .art-ear { left: 140px; top: 321px; width: 560px; height: 532px;
    background: radial-gradient(ellipse 42% 52% at 58% 50%, rgba(242,138,28,.55), rgba(226,35,26,.45) 45%, rgba(31,95,181,.18) 75%, transparent 100%); }
  .art-ground { left: 0; top: 978px; width: 848px; height: 222px;
    background: linear-gradient(180deg, rgba(255,255,255,0) 0%, rgba(228,90,143,.25) 30%, rgba(226,35,26,.75) 70%, var(--art-red) 85%),
                linear-gradient(90deg, var(--art-orange), var(--art-red) 40%, var(--art-blue) 65%, var(--art-red)); }
  .credits { position: absolute; left: 36px; top: 702px; font-size: 20.5px; line-height: 24.5px; }
  .dates { position: absolute; left: 36px; top: 848px; font-size: 20.5px; line-height: 24.5px; }
  .badge { position: absolute; left: 610px; top: 811px; width: 202px; height: 202px; border-radius: 50%; background: var(--badge); color: var(--badge-text); text-align: center; }
  .badge-inner { position: absolute; left: 0; right: 0; top: 36px; transform: rotate(-5deg); }
  .badge-main { font-weight: 700; font-size: 38px; line-height: 38px; }
  .badge-note { margin-top: 8px; font-size: 19px; line-height: 21px; }
</style>
</head>
<body>
<main class="poster">
  <svg class="title" viewBox="0 0 772 120" aria-label="Ohrwürmer">
    <text x="0" y="112" font-size="126" textLength="772" lengthAdjust="spacingAndGlyphs">OHRWÜRMER</text>
  </svg>
  <p class="subtitle">von Rossano bis Brennwald<br>für Chor und sinfonisches Blasorchester</p>

  <div class="art art-birds" role="img" aria-label="Bunte Kolibris im Flug"></div>
  <div class="art art-ear" role="img" aria-label="Farbiges Ohr mit fliegenden Musiknoten"></div>
  <div class="art art-ground" role="img" aria-label="Farbenfroher Boden mit Notenschlüssel, Noten und Schmetterlingen"></div>

  <p class="credits">
    Cantabile Chor Seetal (D)<br>
    Gemischter Chor Lindau-Au (Ch)<br>
    Le C(h)oeur Talbach-Wiesen (Ch)<br>
    Musikverein Hornbach (D)<br>
    Leitung: Mara Feldhofer / Jonas Brandl
  </p>
  <p class="dates">
    19. November 2017, 17:00 Uhr,<br>
    Kirche St. Martin Seetal<br>
    26. November 2017, 17:00 Uhr,<br>
    Reformierte Kirche Talbach
  </p>

  <div class="badge">
    <div class="badge-inner">
      <div class="badge-main">EINTRITT<br>FREI</div>
      <div class="badge-note">Spende freundlich<br>erbeten</div>
    </div>
  </div>
</main>
</body>
</html>
```